An hotel welcome folder kit
luxury suites in NYC
An hotel  welcome folder kit -
Creative Brief
We are looking for to set up a beautiful welcome folder for our suites guests. This folder will be placed in the room on the bed. Within this folder they will find the whole info they need in order to get around the building they are staying in,about our services, the location. amenities, attractions etc. here is some info about what our business about: Morvane Lodgings offers various luxury vacation suites in beautiful luxury residential buildings around Manhattan and are rented out to tourists on a short term basis a la a hotel. The suites and buildings come fully equipped with all the necessary amenities and more: - wireless internet & high definition television with digital cable in unit - On site laundry room - Fantastic fully equipped gym - Residential lounge area with billiards table - Amazing roof deck with breathtaking views of the city.
our suites guests.
The welcome kit is a folder that has a one pocket on the right hand side of the folder inside. in this pocket we will place the pages with the info the guests need to know. on the left hand side inside the folder we will pitch our hotel concept (1-2 short sentences). on the cover of the folder we would like to see our logo and the name of the hotel the logo file is attached. what do we need from you: 1.a design of the folder based on our logo (colors ans font) : cover , left hand side inside the folder, on the back of the folder our contact info 2. a design of a template for the pages that we will place inside the folder (each page has its own topic for example: one page is about our services, the second page is info about attractions in the city..etc) important: the design should present out consept of luxury , high end style, Cutting-Edge Unique/Creative,Clean/Simple, Sophisticated. info about the logo: Brown #CFBA76 R:207 G:186 B:118 Font:Rage Italic Font2: Arial tagline: Arial dark Gray: #333333 R:51 G:51 B:51 Thanks a lot!!!

```html
<!DOCTYPE html>
<html lang="en">
<head>
<meta charset="utf-8">
<title>Morvane Lodgings – Welcome Folder Inside Spread</title>
<link href="https://fonts.googleapis.com/css2?family=Great+Vibes&family=Cormorant+Garamond:wght@400;500&family=Open+Sans:ital,wght@0,400;0,700;1,400;1,700&display=swap" rel="stylesheet">
<style>
  :root {
    --gold: #cfba76;
    --gold-deep: #a88a45;
    --brown-text: #7a5a24;
    --brown-body: #5a4526;
    --cream: #efe6d2;
    --ink: #0c0c0c;
    --white: #ffffff;
    --grey-label: #333333;
  }
  * { margin: 0; padding: 0; box-sizing: border-box; }
  html, body { width: 1200px; height: 833px; overflow: hidden; background: #fff; }
  .canvas { position: relative; width: 1200px; height: 833px; overflow: hidden; font-family: "Open Sans", Arial, sans-serif; }

  .spread-label { position: absolute; top: 4px; font-size: 13px; color: var(--grey-label); }
  .spread-label.inside-1 { left: 6px; }
  .spread-label.inside-2 { left: 468px; }

  .title-band { position: absolute; left: 0; top: 22px; width: 1200px; height: 50px;
    background: linear-gradient(to bottom, #f7f1e4, #ece1c8); border-bottom: 3px solid var(--gold); }
  .title-band h1 { position: absolute; left: 0; right: 0; top: 6px; padding-left: 200px; text-align: center;
    font-family: "Cormorant Garamond", serif; font-weight: 500; font-size: 38px; letter-spacing: 4px; color: var(--gold-deep); }

  /* Inside-1 */
  .panel-left { position: absolute; left: 0; top: 75px; width: 600px; height: 758px; overflow: hidden; }
  .panel-left .room-photo { position: absolute; inset: 0;
    background: radial-gradient(ellipse at 62% 68%, #f1e4c3 0%, #c9b07c 35%, #8f7447 70%, #5c4829 100%); }
  .panel-left .text-wash { position: absolute; inset: 0;
    background: linear-gradient(to right, rgba(240,228,200,.92) 0%, rgba(236,222,190,.75) 45%, rgba(236,222,190,0) 62%); }
  .left-copy { position: absolute; left: 14px; top: 14px; width: 300px; color: var(--brown-body); }
  .section-head { font-family: "Great Vibes", cursive; font-size: 46px; color: var(--brown-text); line-height: 1; margin-left: 4px; }
  .lead { font-weight: 700; font-style: italic; font-size: 13.5px; line-height: 1.3; color: var(--brown-text); margin: 8px 0 12px; }
  .body { font-size: 10.5px; line-height: 1.42; margin-bottom: 10px; }
  .facilities { position: absolute; left: 14px; top: 450px; width: 300px; color: var(--brown-body); }
  .amenities-intro { font-weight: 700; font-size: 10.5px; line-height: 1.4; margin-bottom: 2px; }
  .amenities { list-style: none; font-size: 10.5px; line-height: 1.45; }
  .amenities li::before { content: "• "; }

  /* Inside-2 */
  .panel-right { position: absolute; left: 600px; top: 75px; width: 600px; height: 758px; background: var(--ink); overflow: hidden; }
  .panel-right svg { position: absolute; left: 0; top: 0; }
  .brand { position: absolute; left: 30px; top: 70px; color: var(--white); }
  .brand-name { font-family: "Great Vibes", cursive; font-size: 40px; line-height: 1; color: var(--white); display: flex; align-items: center; gap: 10px; }
  .brand-dot { width: 14px; height: 14px; border-radius: 50%; background: var(--gold); }
  .brand-tagline { font-size: 12px; margin: 4px 0 0 26px; }
  .stay-line { position: absolute; right: 26px; top: 70px; text-align: right; color: var(--white);
    font-weight: 700; font-style: italic; font-size: 18px; line-height: 1.25; text-transform: uppercase; }
  .city-photo { position: absolute; left: 324px; top: 190px; width: 276px; height: 460px;
    background: linear-gradient(160deg, #d9d6cf 0%, #9a9893 30%, #5d5c58 60%, #2c2b29 100%); }
  .promo { position: absolute; left: 36px; top: 300px; width: 270px; color: var(--white); }
  .promo h2 { font-style: italic; font-weight: 700; font-size: 16px; line-height: 1.3; margin-bottom: 14px; }
  .promo p { font-size: 10px; line-height: 1.45; margin-bottom: 8px; }
</style>
</head>
<body>
<div class="canvas">
  <span class="spread-label inside-1">Inside-1</span>
  <span class="spread-label inside-2">Inside-2</span>

  <header class="title-band"><h1>LUXURY SUITES IN NYC</h1></header>

  <section class="panel-left">
    <div class="room-photo" role="img" aria-label="Sepia-toned photograph of an elegant suite interior with draped windows, a lamp and a round table with a long cloth and flowers"></div>
    <div class="text-wash"></div>
    <div class="left-copy">
      <h2 class="section-head">Suites</h2>
      <p class="lead">If you are dreaming of rest, relaxation and tranquility in a stunning setting with truly personal service, then we can make your Morvane Lodgings come true.</p>
      <p class="body">Morvane Lodgings is the place where style, opulence, and perfection meet a world of beauty and tradition. They represent a new concept of sanctuary with just four luxury suites that have a unique personality, and combine courtesy and warm service with authentic tradition. The suites were designed for the discerning guest who is able to appreciate a singular kind of comfort, class, space and tranquility.</p>
      <p class="body">Our Luxury Suites, and the staff serving them are unique, and we are dedicated to making our guests feel unique too.</p>
      <p class="body">Each Luxury Suite is designed in the traditional city style, and has its own terrace with a Swimming Pool or Jacuzzi overlooking the skyline and the river. Our suites have stayed true to the original style of the district and represent an inimitable sample of traditional local architecture. The privileged location of the suites provides a nearly stay-free access.</p>
    </div>
    <div class="facilities">
      <h2 class="section-head">Facilities</h2>
      <p class="lead">Morvane Lodgings offers various luxury vacation suites in beautiful luxury residential buildings around Manhattan and are rented out to tourists on a short term basis a la a hotel.</p>
      <p class="amenities-intro">The suites and buildings come fully equipped with all the necessary amenities and more:</p>
      <ul class="amenities">
        <li>Wireless internet &amp; high definition television with digital cable in unit</li>
        <li>On site laundry room</li>
        <li>Fantastic fully equipped gym</li>
        <li>Residential lounge area with billiards table</li>
        <li>Amazing roof deck with breathtaking views of the city.</li>
      </ul>
    </div>
  </section>

  <section class="panel-right">
    <div class="city-photo" role="img" aria-label="Photograph of Manhattan skyscrapers seen from above"></div>
    <svg width="600" height="758" viewBox="0 0 600 758" aria-hidden="true">
      <defs>
        <linearGradient id="tanSweep" x1="0" y1="0" x2="1" y2="0">
          <stop offset="0" stop-color="#e9dcbc"/>
          <stop offset="1" stop-color="#b99c5c"/>
        </linearGradient>
      </defs>
      <path d="M0 0 H600 V24 C420 26 230 60 0 150 Z" fill="url(#tanSweep)"/>
      <path d="M0 170 C230 76 420 40 600 40" fill="none" stroke="var(--gold)" stroke-width="3"/>
      <path d="M324 190 C420 150 520 130 600 128 V190 Z" fill="var(--ink)"/>
      <path d="M0 758 V700 C200 650 420 640 600 600 V758 Z" fill="var(--ink)"/>
      <path d="M0 700 C200 650 420 640 600 600" fill="none" stroke="var(--white)" stroke-width="4"/>
    </svg>
    <div class="brand">
      <div class="brand-name"><span class="brand-dot"></span>Morvane Lodgings</div>
      <div class="brand-tagline">luxury suites in NYC</div>
    </div>
    <div class="stay-line">A wonderfull<br>restful stay</div>
    <div class="promo">
      <h2>Lorem ipsum dolor sit amet,<br>Sed varius suscipit neque</h2>
      <p>Lorem ipsum dolor sit amet, consectetur adipiscing elit. Donec enim augue, tempor molestie auctor eu, elementum eu ante. Sed varius suscipit neque et aliquam. Nam nec leo sed ipsum suscipit fringilla. Cras fermentum nisi et amet erat accumsan, integer a lobortis vitae.</p>
      <p>Pellentesque habitant morbi tristique senectus et netus et malesuada fames ac turpis egestas. Cras malesuada fermentum urna, vitae ultricies libero. Aenean tincidunt enim, at faucibus justo tempor sit amet.</p>
    </div>
  </section>
</div>
</body>
</html>
```